Meridale Cleaning Services

In need of a business card design suited for a growing cleaning company.

We offer our cleaning and maintenance services to a wide range of clients including but not limited to the following: constuction industry, hospitality, commercial, industrial and domestic

I want the card to be very noticable, i would like people to say 'hey, great card!' when i hand them my card.double sided would be nice

we want our business to come across as exceedingly professional and innovative (different).

a contemporary design is what we have in mind
we want to present an image of a quality business with a high standard of excellence in consistent service.

i just really need a card that persuades top end quality,
our business is very certified and also strives towards environmentaly friendly alternatives
Updates

hey sorry, i have uploaded my company logo design and name
cheers.

hey guys i have added my company logo/name file on my brief page. many thanks

sorry guys a typo in the brief..
address is Tolley Rd. not Tolly Rd
thanks

Industry/Entity Type

Industrial

Requirements
Must have
• company name: meridale cleaning services
operations manager: Colm Varetti
Tel: (02)9373 6204
Fax: (02)8645 7712
Mob: 0438571490

address: 47 Tolly RD Pymble NSW 2073
Postal Adress: PO Box 5832 North Ryde NSW 2113
email: meridaleclean@wexanet.com.au
website: meridalecleaningservices.com.au

```html
<!DOCTYPE html>
<html lang="en">
<head>
<meta charset="utf-8">
<title>Meridale Cleaning Services – Business Card</title>
<link rel="stylesheet" href="https://fonts.googleapis.com/css2?family=Roboto:wght@400;700&display=swap">
<style>
  :root {
    --brand-blue: #1f6fba;
    --swoosh-blue: #1b78c2;
    --leaf-green: #6aab3f;
    --ink: #2b2b2b;
    --muted: #5a5a5a;
    --card-top: #ffffff;
    --card-bottom: #e4e5e6;
    --card-edge: #c9cacb;
    --page: #ffffff;
  }
  * { margin: 0; padding: 0; box-sizing: border-box; }
  html, body {
    width: 1121px; height: 1200px; overflow: hidden;
    background: var(--page);
    font-family: "Roboto", Arial, sans-serif;
  }
  .card {
    position: absolute;
    left: 152px;
    width: 809px;
    border: 1px solid var(--card-edge);
    border-radius: 22px;
    background: linear-gradient(180deg, var(--card-top) 0%, var(--card-bottom) 100%);
    overflow: hidden;
  }
  .card--front { top: 118px; height: 461px; }
  .card--back { top: 717px; height: 412px; }

  .swoosh { position: absolute; inset: 0; width: 100%; height: 100%; }

  .brand { position: absolute; color: var(--brand-blue); font-weight: 700; }
  .brand__mark {
    position: absolute; width: 108px; height: 108px; border-radius: 50%;
    background: var(--brand-blue);
  }
  .brand__name { position: absolute; font-size: 80px; line-height: 1; white-space: nowrap; letter-spacing: -1px; }
  .brand__sub { position: absolute; font-size: 28px; line-height: 1; white-space: nowrap; }

  .card--front .brand__mark { left: 58px; top: 41px; }
  .card--front .brand__name { left: 228px; top: 38px; }
  .card--front .brand__sub { left: 248px; top: 126px; }

  .card--back .brand__mark { left: 153px; top: 144px; }
  .card--back .brand__name { left: 313px; top: 152px; }
  .card--back .brand__sub { left: 330px; top: 237px; }

  .person { position: absolute; left: 77px; top: 202px; }
  .person__name { font-size: 27px; font-weight: 700; color: var(--ink); }
  .person__role { font-size: 22px; color: var(--muted); margin-top: 4px; }

  .contact { position: absolute; left: 77px; top: 280px; list-style: none; font-size: 14.5px; color: var(--muted); }
  .contact li { line-height: 20.5px; }
  .contact li.gap { margin-top: 2px; }
  .contact b { color: var(--ink); font-weight: 700; }
</style>
</head>
<body>

<section class="card card--front" aria-label="Card front">
  <svg class="swoosh" viewBox="0 0 809 461" preserveAspectRatio="none" aria-hidden="true">
    <path d="M410,461 C610,405 760,290 809,32 L809,461 Z" fill="var(--leaf-green)"/>
    <path d="M423,461 C620,408 768,300 809,48 L809,461 Z" fill="var(--swoosh-blue)"/>
  </svg>

  <div class="brand">
    <span class="brand__mark"></span>
    <span class="brand__name">Meridale</span>
    <span class="brand__sub">CLEANING SERVICES</span>
  </div>

  <div class="person">
    <p class="person__name">Colm Varetti</p>
    <p class="person__role">Area manager</p>
  </div>

  <ul class="contact">
    <li><b>Tel:</b> (02) 9373 6204</li>
    <li><b>Fax:</b> (02) 8645 7712</li>
    <li><b>Mob:</b> 0438 571 490</li>
    <li class="gap"><b>Address:</b> 47 Tolley RD Pymble NSW 2073</li>
    <li class="gap"><b>Postal Adress:</b> PO Box 5832 North Ryde NSW 2113</li>
    <li><b>Email:</b> colm@meridalecleaningservices.com.au</li>
    <li><b>Website:</b> meridalecleaningservices.com.au</li>
  </ul>
</section>

<section class="card card--back" aria-label="Card back">
  <div class="brand">
    <span class="brand__mark"></span>
    <span class="brand__name">Meridale</span>
    <span class="brand__sub">CLEANING SERVICES</span>
  </div>
</section>

</body>
</html>
```